Corvath Properties Business Card Design

We would now like to design business cards with the new Corvath Properties logo

Target Market(s)

Professional

Industry/Entity Type

Professional services

Contact Information for Business Card

Employee name, title, phone number, email address, corporate office address and logo.

Font styles to use
Sans Serif

Colors
0054AA
0677BA
7BADD7
CADEEF
E8F1F8

Requirements
Must have
• My logo
Should not have
• any other pictures or images besides my logo

```html
<!DOCTYPE html>
<html lang="en">
<head>
<meta charset="UTF-8">
<title>Corvath Properties — Business Card</title>
<link href="https://fonts.googleapis.com/css2?family=Oswald:wght@500&family=Roboto:wght@400&display=swap" rel="stylesheet">
<style>
  :root {
    --brand-blue: #0a74d6;
    --card-white: #fbfbfb;
    --ink-white: #ffffff;
    --backdrop: #e8f1f8;
  }
  * { margin: 0; padding: 0; box-sizing: border-box; }
  html, body {
    width: 1200px; height: 874px; overflow: hidden;
    background: var(--backdrop);
  }
  .canvas {
    position: relative; width: 1200px; height: 874px;
  }
  .card {
    position: absolute; left: 280px; width: 640px; height: 366px;
    box-shadow: 0 6px 18px rgba(0, 40, 90, 0.18);
  }
  /* Front */
  .card-front { top: 51px; background: var(--card-white); }
  .front-frame {
    position: absolute; inset: 20px;
    border: 6px solid var(--brand-blue);
  }
  .wordmark {
    position: absolute; inset: 0;
    display: flex; align-items: center; justify-content: center; gap: 18px;
  }
  .wordmark-square {
    width: 58px; height: 58px; background: var(--brand-blue);
  }
  .wordmark-name {
    font-family: 'Oswald', sans-serif; font-weight: 500;
    font-size: 44px; line-height: 1; letter-spacing: 1px;
    color: var(--brand-blue); text-transform: uppercase;
  }
  /* Back */
  .card-back { top: 457px; background: var(--brand-blue); }
  .back-frame { position: absolute; inset: 0; }
  .identity {
    position: absolute; right: 336px; top: 148px; text-align: right;
    color: var(--ink-white);
  }
  .person-name {
    font-family: 'Oswald', sans-serif; font-weight: 500;
    font-size: 30px; line-height: 1; text-transform: uppercase;
  }
  .person-title {
    font-family: 'Roboto', sans-serif; font-size: 15px; margin-top: 2px;
  }
  .divider {
    position: absolute; left: 318px; top: 132px; width: 2px; height: 102px;
    background: var(--ink-white);
  }
  .contact-list {
    position: absolute; left: 338px; top: 136px; list-style: none;
    font-family: 'Roboto', sans-serif; font-size: 15px; line-height: 20px;
    color: var(--ink-white);
  }
  .contact-list li { display: flex; gap: 8px; }
  .contact-list svg { flex: none; width: 13px; height: 13px; margin-top: 3px; fill: var(--ink-white); }
</style>
</head>
<body>
<main class="canvas">
  <section class="card card-front">
    <div class="front-frame"></div>
    <div class="wordmark">
      <span class="wordmark-square"></span>
      <span class="wordmark-name">Corvath Properties</span>
    </div>
  </section>

  <section class="card card-back">
    <svg class="back-frame" width="640" height="366" viewBox="0 0 640 366">
      <g stroke="#ffffff" stroke-width="5" fill="none">
        <polyline points="26,120 26,24 300,24"/>
        <polyline points="336,24 614,24 614,70"/>
        <line x1="614" y1="104" x2="614" y2="258"/>
        <polyline points="614,292 614,342 340,342"/>
        <polyline points="304,342 26,342 26,156"/>
      </g>
    </svg>
    <div class="identity">
      <div class="person-name">Daniel Brooks</div>
      <div class="person-title">President</div>
    </div>
    <div class="divider"></div>
    <ul class="contact-list">
      <li>
        <svg viewBox="0 0 24 24"><path d="M12 2a7 7 0 0 0-7 7c0 5 7 13 7 13s7-8 7-13a7 7 0 0 0-7-7zm0 9.5A2.5 2.5 0 1 1 12 6.5a2.5 2.5 0 0 1 0 5z"/></svg>
        <span>2190 Willowmere Lane<br>Fairbanks, Alaska 99709</span>
      </li>
      <li>
        <svg viewBox="0 0 24 24"><path d="M6.6 10.8a15 15 0 0 0 6.6 6.6l2.2-2.2a1 1 0 0 1 1-.25 11.4 11.4 0 0 0 3.6.57 1 1 0 0 1 1 1V20a1 1 0 0 1-1 1A17 17 0 0 1 3 4a1 1 0 0 1 1-1h3.5a1 1 0 0 1 1 1c0 1.25.2 2.45.57 3.57a1 1 0 0 1-.25 1z"/></svg>
        <span>369-555-0142</span>
      </li>
      <li>
        <svg viewBox="0 0 24 24"><path d="M2 5h20v14H2zm2 2v.5l8 5 8-5V7l-8 5z"/></svg>
        <span>info@corvathproperties.com</span>
      </li>
      <li>
        <svg viewBox="0 0 24 24"><circle cx="12" cy="12" r="10"/></svg>
        <span>corvathproperties.com</span>
      </li>
    </ul>
  </section>
</main>
</body>
</html>
```